RM BIZ CARDS

Hi,

Is it possible to see a one sided version (with logo and info) as well as a two-sided version (front side w/logo and back side with info)?
How do we choose card stock and finish once we approve a design?

We would like the following info included:

Peter Lowell
Rosfeld Talent Media
4127 Marwick Lane, Suite 300
Los Angeles, CA 90041
(323) 555-0148
peter@rosfeldtalentmedia.example

```html
<!DOCTYPE html>
<html lang="en">
<head>
<meta charset="utf-8">
<title>Rosfeld Talent Media – Business Cards</title>
<link rel="stylesheet" href="https://fonts.googleapis.com/css2?family=Jost:wght@300;400;600&display=swap">
<style>
  :root {
    --ink: #0d0d0d;
    --paper: #ffffff;
    --stage: #e6e6e4;
    --text: #1a1a1a;
    --muted: #333333;
  }
  * { box-sizing: border-box; margin: 0; padding: 0; }
  html, body { width: 1200px; height: 873px; overflow: hidden; }
  body {
    background: var(--stage);
    font-family: "Jost", sans-serif;
    color: var(--text);
    display: flex;
    align-items: center;
    justify-content: center;
    gap: 40px;
  }
  .card {
    width: 540px;
    height: 309px;
    position: relative;
    box-shadow: 0 6px 22px rgba(0,0,0,0.18);
    overflow: hidden;
  }
  .card--front { background: var(--paper); }
  .card--back {
    background: var(--ink);
    display: flex;
    flex-direction: column;
    align-items: center;
    justify-content: center;
    gap: 16px;
  }

  /* brand mark */
  .brand {
    display: flex;
    flex-direction: column;
    align-items: center;
    gap: 10px;
  }
  .brand__dot {
    width: 34px; height: 34px;
    border-radius: 50%;
    border: 2px solid currentColor;
  }
  .brand__name {
    font-weight: 300;
    font-size: 20px;
    letter-spacing: 0.16em;
    text-transform: uppercase;
  }
  .card--front .brand {
    position: absolute;
    top: 26px; left: 0; right: 0;
    color: var(--muted);
  }
  .card--back .brand { color: var(--paper); }
  .card--back .brand__dot { width: 44px; height: 44px; }
  .card--back .brand__name { font-size: 26px; }

  /* name band */
  .band {
    position: absolute;
    top: 128px; left: 0; right: 0;
    height: 48px;
    background: var(--ink);
    color: var(--paper);
    display: flex;
    align-items: center;
    justify-content: space-between;
    padding: 0 32px;
  }
  .band__person { font-weight: 600; font-size: 19px; }
  .band__company { font-weight: 400; font-size: 15px; letter-spacing: 0.02em; }
  .band__notch {
    position: absolute;
    bottom: -8px;
    width: 0; height: 0;
    border-left: 8px solid transparent;
    border-right: 8px solid transparent;
    border-top: 8px solid var(--ink);
  }
  .band__notch--left { left: 56px; }
  .band__notch--mid { left: 262px; }
  .band__notch--right { left: 440px; }

  /* contact row */
  .contacts {
    position: absolute;
    top: 206px; left: 0; right: 0;
    display: grid;
    grid-template-columns: 1fr 0.8fr 1.1fr;
    padding: 0 22px;
  }
  .contact {
    display: flex;
    flex-direction: column;
    align-items: center;
    gap: 10px;
    text-align: center;
    font-size: 10.5px;
    line-height: 1.45;
    color: var(--muted);
  }
  .contact__icon { width: 18px; height: 18px; }
  .contact__icon path, .contact__icon rect, .contact__icon polyline {
    fill: none;
    stroke: var(--muted);
    stroke-width: 1.4;
    stroke-linejoin: round;
    stroke-linecap: round;
  }
</style>
</head>
<body>

  <section class="card card--front" aria-label="Card front with contact details">
    <div class="brand">
      <span class="brand__dot"></span>
      <span class="brand__name">Rosfeld Talent</span>
    </div>

    <div class="band">
      <span class="band__person">Peter Lowell</span>
      <span class="band__company">Rosfeld Talent Media</span>
      <span class="band__notch band__notch--left"></span>
      <span class="band__notch band__notch--mid"></span>
      <span class="band__notch band__notch--right"></span>
    </div>

    <div class="contacts">
      <div class="contact">
        <svg class="contact__icon" viewBox="0 0 18 18" aria-hidden="true">
          <path d="M2 9 L9 2.5 L16 9"/>
          <path d="M4 7.5 V16 H14 V7.5"/>
          <rect x="7.5" y="11" width="3" height="5"/>
        </svg>
        <span>4127 Marwick Lane, Suite 300<br>Los Angeles, CA 90041</span>
      </div>
      <div class="contact">
        <svg class="contact__icon" viewBox="0 0 18 18" aria-hidden="true">
          <path d="M4 2.5 L7 2.5 L8 6 L6 7.5 C7 10 8 11 10.5 12 L12 10 L15.5 11 L15.5 14 C15.5 15 14.5 15.5 13.5 15.5 C7.5 15 3 10.5 2.5 4.5 C2.5 3.5 3 2.5 4 2.5 Z"/>
        </svg>
        <span>(323) 555-0148</span>
      </div>
      <div class="contact">
        <svg class="contact__icon" viewBox="0 0 18 18" aria-hidden="true">
          <rect x="2" y="4" width="14" height="10"/>
          <polyline points="2,4 9,10 16,4"/>
        </svg>
        <span>peter@rosfeldtalentmedia.example</span>
      </div>
    </div>
  </section>

  <section class="card card--back" aria-label="Card back with brand name">
    <div class="brand">
      <span class="brand__dot"></span>
      <span class="brand__name">Rosfeld Talent</span>
    </div>
  </section>

</body>
</html>
```